Pages toward Inner Calm - book cover

12/18 update: Please read the entire brief. I don’t love anything that has been provided up to today. Please use the graphics and colors I’ve attached!!!! Show me your creations.

I am looking for a book cover design. It is a mental health journal. Needs to be very warm, inviting, calming. I’m very interested in new creative ideas. It will be wire-o bound and also in hard copy front and back. Use the graphic and colors I already have attached to this file. It’s called “Pages Toward Inner Calm”. Self means soul or spirit or center. The idea of integration may be a fit here in some way. If some words need to be emphasized in the design, “Self” and “QRM” would be the most important. size 6"x9". The words on the front can be smaller and more inviting then they would normally be on a fiction paperback.

Update 12/16: I am not excited about any of the submissions so far. I’m looking forward to seeing more options.

Target Market(s)

Adults 30-60. Male and female. People who like to learn. People wanting to heal. Middle and upper income.

Industry/Entity Type

Mental health. Wellness

Font styles to use
Other font styles liked:
• Whatever font is used in my logo. i don’t know the name. I also would be open to a different font if it was warm, inviting, and calm.

Colors
0094D4
00A9DD
6FCCEA
C7EBF8
E9F6FB

Requirements
Must have
• My logo colors. The words “Pages Toward Inner Calm” and “A 13-Week QRM Exploration”
Nice to have
• I’d like to see some creative ideas. More abstract than realistic.
Should not have
• No realist art or photos.

```html
<!DOCTYPE html>
<html lang="en">
<head>
<meta charset="utf-8">
<title>Pages toward Inner Calm – Book Cover</title>
<link href="https://fonts.googleapis.com/css2?family=Marcellus&family=Montserrat:wght@700&family=Mrs+Saint+Delafield&display=swap" rel="stylesheet">
<style>
  :root {
    --page-bg: #ffffff;
    --blue-deep: #0094d4;
    --blue-mid: #00a9dd;
    --blue-soft: #6fccea;
    --blue-pale: #c7ebf8;
    --blue-mist: #e9f6fb;
    --ink: #0b3a52;
    --white: #ffffff;
  }
  * { margin: 0; padding: 0; box-sizing: border-box; }
  html, body {
    width: 1200px; height: 675px; overflow: hidden;
    background: var(--page-bg);
  }
  .canvas { position: relative; width: 1200px; height: 675px; }
  .book-cover {
    position: absolute; left: 389px; top: 0;
    width: 422px; height: 675px;
    background: radial-gradient(ellipse at 50% 50%, #f4fbfd 0%, var(--blue-mist) 75%);
    overflow: hidden;
  }
  .title-main {
    position: absolute; left: 0; right: 0; top: 18px;
    text-align: center;
    font-family: "Marcellus", serif; font-weight: 400;
    font-size: 47px; letter-spacing: 1px;
    color: var(--blue-deep);
    line-height: 1;
  }
  .title-script {
    position: absolute; left: 150px; top: 52px;
    font-family: "Mrs Saint Delafield", cursive;
    font-size: 72px; color: var(--ink);
    line-height: 1;
  }
  .brand {
    position: absolute; left: 266px; top: 134px;
    display: flex; align-items: center; gap: 6px;
    white-space: nowrap;
  }
  .brand-dot {
    width: 9px; height: 9px; border-radius: 50%;
    background: var(--ink);
  }
  .brand-name {
    font-family: "Marcellus", serif;
    font-size: 10px; letter-spacing: 1px;
    text-transform: uppercase; color: var(--ink);
  }
  .floral-art {
    position: absolute; left: 95px; top: 153px;
    width: 213px; height: 397px;
    border-radius: 46% 46% 44% 44%;
    background:
      radial-gradient(circle at 35% 20%, var(--blue-pale) 0%, transparent 24%),
      radial-gradient(circle at 50% 38%, var(--blue-mid) 0%, transparent 32%),
      radial-gradient(circle at 38% 62%, var(--blue-soft) 0%, transparent 28%),
      radial-gradient(circle at 68% 66%, var(--blue-deep) 0%, transparent 30%),
      radial-gradient(circle at 40% 82%, var(--blue-soft) 0%, transparent 28%),
      radial-gradient(ellipse at 55% 50%, rgba(111,204,234,0.55) 0%, transparent 72%);
  }
  .title-vertical {
    position: absolute; left: 186px; top: 206px;
    width: 50px;
    font-family: "Montserrat", sans-serif; font-weight: 700;
    font-size: 78px; line-height: 83px;
    color: var(--white); text-align: center;
    text-shadow: 0 1px 4px rgba(0,80,120,0.18);
  }
  .title-vertical span { display: block; }
  .subtitle {
    position: absolute; left: 0; right: 0; top: 574px;
    text-align: center;
    font-family: "Marcellus", serif;
    font-size: 29px; color: var(--blue-deep);
    line-height: 1;
  }
  .author-band {
    position: absolute; left: 0; right: 0; bottom: 0;
    height: 45px; background: var(--blue-deep);
    display: flex; align-items: center; justify-content: center;
  }
  .author-name {
    font-family: "Marcellus", serif;
    font-size: 28px; letter-spacing: 2px;
    color: var(--white); line-height: 1; padding-top: 3px;
  }
</style>
</head>
<body>
  <div class="canvas">
    <section class="book-cover">
      <h1 class="title-main">PAGES TOWARD</h1>
      <div class="title-script">inner</div>
      <div class="brand">
        <span class="brand-dot"></span>
        <span class="brand-name">Lindqvist Wellness</span>
      </div>
      <div class="floral-art" role="img" aria-label="Vertical arrangement of soft flowers and leaves in calm blue tones"></div>
      <div class="title-vertical" aria-label="CALM">
        <span>C</span><span>A</span><span>L</span><span>M</span>
      </div>
      <p class="subtitle">A 13-Week QRM Exploration</p>
      <div class="author-band">
        <span class="author-name">AUTHOR NAME</span>
      </div>
    </section>
  </div>
</body>
</html>
```